New Website for Belcourt Manor at www.belcourt.com.au

A new logo has been designed (through pixel forge) and we now want to align the look and feel of our website at www.belcourt.com.au to the new logo. The content and page names (e.g. Grounds) will remain largely unchanged for the new site, so please submit a new look "Home" page, using our new logo, current text and any photos you choose from the existing gallery at our website. I have also attached the current "Home" page photos.

Industry/Entity Type

Accommodation

Number of Pages Required

1 page

Requirements
Must have
• Logo to be presented on white background.

```html
<!DOCTYPE html>
<html lang="en">
<head>
<meta charset="utf-8">
<title>Belcourt Manor — Home</title>
<link href="https://fonts.googleapis.com/css2?family=Roboto+Condensed:wght@400;700&family=Open+Sans:wght@400;600&family=Lora:ital@1&display=swap" rel="stylesheet">
<style>
:root{
  --blue:#1a9ad6;
  --blue-band:#129ddd;
  --dark:#2f2f2f;
  --darker:#262626;
  --ink:#222;
  --muted:#6b6b6b;
  --light:#f4f4f4;
  --white:#fff;
}
*{box-sizing:border-box;margin:0;padding:0}
html,body{width:1200px;height:4255px;overflow:hidden;background:var(--white)}
body{font-family:"Open Sans",Arial,sans-serif;color:var(--ink)}
.page{position:relative;width:1200px;height:4255px;overflow:hidden}
.abs{position:absolute}
.band{position:absolute;left:0;width:1200px}
.head{font-family:"Roboto Condensed",Arial,sans-serif;font-weight:400;text-transform:uppercase}
.italic{font-family:"Lora",Georgia,serif;font-style:italic}
.btn{position:absolute;display:flex;align-items:center;justify-content:center;font-family:"Roboto Condensed",Arial,sans-serif;font-size:16px;text-transform:uppercase;color:var(--white)}
.btn-blue{background:var(--blue)}
.btn-ghost{border:2px solid rgba(255,255,255,.8);background:rgba(0,0,0,.35)}
.field{position:absolute;background:var(--white);border:1px solid #ccc;font-size:14px;color:#888;padding:0 10px;display:flex;align-items:center}

/* hero */
.hero{top:0;height:672px;background:linear-gradient(180deg,#2a3650 0%,#4a5a72 30%,#3d3426 62%,#2a2118 100%)}
.hero-shade{top:658px;height:14px;background:#555}
.brand{left:85px;top:52px}
.brand-name{font-family:"Roboto Condensed",Arial,sans-serif;font-size:56px;line-height:64px;font-weight:400;color:var(--blue)}
.nav{top:79px;height:34px}
.nav a{position:absolute;top:0;height:34px;display:flex;align-items:center;font-family:"Roboto Condensed",Arial,sans-serif;font-size:16px;color:var(--white);text-decoration:none;text-transform:uppercase}
.nav a.active{background:var(--blue);justify-content:center}
.hero-title{left:0;width:1200px;top:275px;text-align:center;font-family:"Roboto Condensed",Arial,sans-serif;font-size:54px;color:var(--white)}
.hero-rule{top:308px;height:2px;background:rgba(255,255,255,.75)}
.hero-sub{left:170px;width:860px;top:375px;text-align:center;font-size:25px;line-height:46px;color:var(--white)}
.dots{left:540px;top:498px;display:flex;gap:26px}
.dots span{width:16px;height:16px;transform:rotate(45deg);background:var(--white)}
.dots span.on{background:var(--blue);outline:3px solid rgba(255,255,255,.6)}

/* newsletter */
.newsletter{top:672px;height:208px;background:linear-gradient(180deg,#3a3a3a,#2c2c2c)}
.section-title{left:0;width:1200px;text-align:center;font-size:44px;color:var(--blue)}

/* about */
.about{top:880px;height:476px;background:var(--light)}
.about p{position:absolute;left:80px;width:760px;font-size:15px;line-height:26px;color:var(--muted)}
.about p a{color:var(--ink);font-style:italic;text-decoration:underline}
.about-name{left:850px;top:240px;width:305px;text-align:center;font-family:"Roboto Condensed",Arial,sans-serif;font-size:44px;line-height:52px;color:var(--blue)}

/* services */
.services{top:1356px;height:743px;background:linear-gradient(180deg,#3b4350 0%,#2d3038 50%,#36322c 100%)}
.service{position:absolute;width:330px;text-align:center;color:var(--white)}
.service .photo{width:187px;height:187px;border-radius:50%;border:5px solid var(--white);margin:0 auto}
.service h3{font-family:"Roboto Condensed",Arial,sans-serif;font-weight:400;font-size:20px;margin-top:23px}
.service p{font-size:14px;line-height:22px;margin-top:12px;color:#eee}

/* gallery */
.gallery{top:2099px;height:823px;background:var(--white)}
.tile{position:absolute}

/* testimonials */
.testimonials{top:2922px;height:431px;background:linear-gradient(180deg,#3a3a3a,#2b2b2b)}
.quote-name{position:absolute;font-size:15px;color:var(--white)}
.quote-name b{color:var(--blue);font-family:"Lora",Georgia,serif;font-weight:400;text-transform:uppercase}
.quote-box{position:absolute;width:374px;height:119px;border:2px solid rgba(255,255,255,.75);padding:12px 18px;font-size:14px;line-height:23px;color:var(--white)}
.avatar{position:absolute;width:80px;height:80px;border-radius:50%;background:linear-gradient(135deg,#cfcfcf,#8d8d8d);border:3px solid var(--white)}

/* availability */
.availability{top:3353px;height:244px;background:var(--blue-band)}
.select-arrow{position:absolute;right:0;top:0;width:32px;height:100%;background:#111;display:flex;align-items:center;justify-content:center}

/* contact */
.map{left:0;top:3597px;width:599px;height:417px;background:linear-gradient(135deg,#eeeae0,#e2dccb 60%,#f1ebd6)}
.contact{left:599px;top:3597px;width:601px;height:417px;background:#333}

/* footer */
.footer{top:4014px;height:241px;background:var(--darker)}
.foot-nav{position:absolute;top:4067px;font-family:"Roboto Condensed",Arial,sans-serif;font-size:15px;color:var(--white);text-transform:uppercase}
.social{position:absolute;top:4056px;width:42px;height:42px;border-radius:50%;border:2px solid var(--blue)}
.foot-info{position:absolute;top:4177px;font-size:16px;color:var(--white);display:flex;align-items:center;gap:14px}
.foot-icon{width:30px;height:30px;border-radius:50%;background:#3d4d5c;display:flex;align-items:center;justify-content:center}
</style>
</head>
<body>
<main class="page">

  <!-- Hero -->
  <section class="band hero" role="img" aria-label="Evening photograph of a lit timber deck and pool house beside calm water"></section>
  <div class="band hero-shade"></div>
  <div class="abs brand"><span class="brand-name">Belcourt</span></div>
  <nav class="abs nav">
    <a class="active" href="#" style="left:454px;width:94px">Home</a>
    <a href="#" style="left:562px">Availability</a>
    <a href="#" style="left:700px">Mansion</a>
    <a href="#" style="left:811px">Gallery</a>
    <a href="#" style="left:919px">Location</a>
    <a href="#" style="left:1041px">Contact</a>
  </nav>
  <div class="abs hero-rule" style="left:156px;width:100px"></div>
  <div class="abs hero-rule" style="left:980px;width:108px"></div>
  <h1 class="abs hero-title" style="font-weight:400">Lorem ipsum dolor sit amet</h1>
  <p class="abs hero-sub italic">Lorem ipsum dolor sit amet Lorem ipsum dolor sit amet Lorem ipsum dolor sit amet Lorem ipsum dolor sit amet.....</p>
  <div class="abs dots"><span class="on"></span><span></span><span></span></div>

  <!-- Newsletter -->
  <section class="band newsletter">
    <h2 class="abs section-title" style="top:50px;font-family:'Roboto Condensed',Arial,sans-serif;font-weight:400;font-size:42px">News Letter</h2>
    <div class="field" style="left:173px;top:114px;width:315px;height:42px">User Name*</div>
    <div class="field" style="left:508px;top:114px;width:312px;height:42px">Email*</div>
    <div class="btn btn-blue" style="left:843px;top:114px;width:156px;height:42px">Subscribe</div>
  </section>

  <!-- About -->
  <section class="band about">
    <h2 class="abs head" style="left:80px;top:62px;font-size:40px">About</h2>
    <h3 class="abs head" style="left:80px;top:122px;font-size:38px;color:var(--blue)">Belcourt Manor</h3>
    <div class="abs italic" style="left:80px;top:185px;font-size:22px;color:var(--blue)">Palatial estate and luxury resort</div>
    <p style="top:246px">On over 2 manicured garden acres, Belcourt Manor is a unique Gold Coast estate, centrally located in the prestigious rural suburb of Kellmore. &nbsp;<a href="#">More about our Location.</a></p>
    <p style="top:316px">For prices, availability and guest reviews, <a href="#">visit StayHub</a></p>
    <div class="btn btn-blue" style="left:80px;top:377px;width:122px;height:40px">Read More</div>
    <div class="abs about-name">Belcourt Manor</div>
  </section>

  <!-- Services -->
  <section class="band services" role="img" aria-label="Dusk photograph of an outdoor terrace and garden as section background"></section>
  <h2 class="abs head" style="left:0;width:1200px;top:1414px;text-align:center;font-size:44px;color:var(--white)">Services</h2>
  <h3 class="abs head" style="left:0;width:1200px;top:1476px;text-align:center;font-size:44px;color:var(--blue)">We Provide You</h3>
  <div class="service" style="left:79px;top:1583px">
    <div class="photo" role="img" aria-label="Aerial view of the estate with pool and gardens" style="background:linear-gradient(135deg,#7c9a5a,#4f7aa0)"></div>
    <h3>Great Environment</h3>
    <p>Lorem ipsum dolor sit amet, consectetur elit. Fusce semper vitae leo sit amet vehicula. Lorem ipsum dolo...</p>
  </div>
  <div class="service" style="left:434px;top:1583px">
    <div class="photo" role="img" aria-label="House with red tiled roof among trees" style="background:linear-gradient(135deg,#6f9bc8,#b7704e)"></div>
    <h3>Middle of downtown</h3>
    <p>Lorem ipsum dolor sit amet, consectetur elit. Fusce semper vitae leo sit amet vehicula. Lorem ipsum dolo...</p>
  </div>
  <div class="service" style="left:788px;top:1583px">
    <div class="photo" role="img" aria-label="Bright modern kitchen interior" style="background:linear-gradient(135deg,#e6e1d6,#8f6a48)"></div>
    <h3>We Clean Everyday</h3>
    <p>Lorem ipsum dolor sit amet, consectetur elit. Fusce semper vitae leo sit amet vehicula. Lorem ipsum dolo...</p>
  </div>
  <div class="btn btn-ghost" style="left:180px;top:1932px;width:128px;height:40px">Read More</div>
  <div class="btn btn-ghost" style="left:535px;top:1932px;width:128px;height:40px">Read More</div>
  <div class="btn btn-ghost" style="left:889px;top:1932px;width:128px;height:40px">Read More</div>
  <div class="btn btn-blue" style="left:539px;top:2006px;width:122px;height:40px">View All</div>

  <!-- Gallery -->
  <section class="band gallery">
    <h2 class="abs section-title head" style="top:60px">Gallery</h2>
    <div class="abs italic" style="left:0;width:1200px;top:120px;text-align:center;font-size:20px;color:var(--blue)">Lorem ipsum dolor sit amet.....</div>
  </section>
  <div class="tile" role="img" aria-label="Entrance hall with curved staircase" style="left:79px;top:2281px;width:517px;height:346px;background:linear-gradient(135deg,#e9e2d4,#b88e6a)"></div>
  <div class="tile" role="img" aria-label="Lounge room with sofas" style="left:610px;top:2281px;width:250px;height:167px;background:linear-gradient(135deg,#7a5c40,#3e4b66)"></div>
  <div class="tile" role="img" aria-label="Timber kitchen" style="left:871px;top:2281px;width:250px;height:167px;background:linear-gradient(135deg,#a46a3a,#d9cdb8)"></div>
  <div class="tile" role="img" aria-label="Hallway with glass doors" style="left:610px;top:2460px;width:250px;height:167px;background:linear-gradient(135deg,#e2b34a,#8a6640)"></div>
  <div class="tile" role="img" aria-label="Bedroom with ceiling fan" style="left:871px;top:2460px;width:250px;height:167px;background:linear-gradient(135deg,#c9b79a,#6d5038)"></div>
  <div class="tile" role="img" aria-label="Dimmed room photo with zoom overlay" style="left:79px;top:2641px;width:247px;height:168px;background:linear-gradient(135deg,#3c3c3c,#1f1f1f)">
    <svg class="abs" style="left:108px;top:68px" width="32" height="32" viewBox="0 0 32 32"><circle cx="13" cy="13" r="9" fill="none" stroke="#fff" stroke-width="3"/><path d="M20 20l9 9M13 9v8M9 13h8" stroke="#fff" stroke-width="3"/></svg>
  </div>
  <div class="tile" role="img" aria-label="Bedroom with dark bedding" style="left:340px;top:2641px;width:250px;height:168px;background:linear-gradient(135deg,#d9d4cc,#4e4038)"></div>
  <div class="tile" role="img" aria-label="Twin bedroom" style="left:610px;top:2641px;width:250px;height:168px;background:linear-gradient(135deg,#ddd2c0,#8c5f44)"></div>
  <div class="tile" role="img" aria-label="Upstairs landing with railing" style="left:871px;top:2641px;width:250px;height:168px;background:linear-gradient(135deg,#a57a52,#efe6d6)"></div>
  <div class="btn btn-blue" style="left:539px;top:2823px;width:122px;height:40px">View All</div>

  <!-- Testimonials -->
  <section class="band testimonials" role="img" aria-label="Darkened interior photograph as section background">
    <h2 class="abs section-title head" style="top:65px">Testimonials</h2>
  </section>
  <div class="quote-name" style="left:204px;top:3075px"><b>Daniel Hart</b> &nbsp;| &nbsp;CUSTOMER</div>
  <div class="avatar" role="img" aria-label="Guest portrait" style="left:96px;top:3109px"></div>
  <div class="quote-box" style="left:199px;top:3112px">“ Lorem ipsum dolor sit amet, consectetur elit. Fusce semper vitae leo sit amet vehicula. Lorem ipsum dolovitae leo sit amet vehicula. Lorem ipsum dolo..”</div>
  <div class="quote-name" style="left:723px;top:3075px"><b>Daniel Hart</b> &nbsp;| &nbsp;CUSTOMER</div>
  <div class="avatar" role="img" aria-label="Guest portrait" style="left:618px;top:3109px"></div>
  <div class="quote-box" style="left:718px;top:3112px">“ Lorem ipsum dolor sit amet, consectetur elit. Fusce semper vitae leo sit amet vehicula. Lorem ipsum dolovitae leo sit amet vehicula. Lorem ipsum dolo..”</div>

  <!-- Check availability -->
  <section class="band availability">
    <h2 class="abs head" style="left:0;width:1200px;top:60px;text-align:center;font-size:44px;color:var(--white)">Check Availability</h2>
    <div class="field" style="left:77px;top:139px;width:241px;height:37px">Check in</div>
    <div class="field" style="left:332px;top:139px;width:241px;height:37px">Check out</div>
    <div class="field" style="left:587px;top:139px;width:168px;height:37px">Adults<span class="select-arrow"><svg width="10" height="6"><path d="M0 0h10L5 6z" fill="#fff"/></svg></span></div>
    <div class="field" style="left:769px;top:139px;width:167px;height:37px">Children<span class="select-arrow"><svg width="10" height="6"><path d="M0 0h10L5 6z" fill="#fff"/></svg></span></div>
    <div class="btn" style="left:956px;top:139px;width:156px;height:37px;background:#0c0c0c">Book Now</div>
  </section>

  <!-- Map and contact -->
  <div class="abs map" role="img" aria-label="Street map of the estate's neighbourhood"></div>
  <section class="abs contact">
    <h2 class="abs head" style="left:82px;top:38px;font-size:44px;color:var(--white)">Contact</h2>
    <div class="field" style="left:76px;top:97px;width:216px;height:40px">Name*</div>
    <div class="field" style="left:306px;top:97px;width:213px;height:40px">Email*</div>
    <div class="field" style="left:76px;top:153px;width:443px;height:40px">Subject*</div>
    <div class="field" style="left:76px;top:207px;width:443px;height:105px;align-items:flex-start;padding-top:8px">Message*</div>
    <div class="btn" style="left:238px;top:332px;width:133px;height:37px;background:#0c0c0c;letter-spacing:3px">Submit</div>
  </section>

  <!-- Footer -->
  <footer class="band footer"></footer>
  <span class="foot-nav" style="left:80px">Home</span>
  <span class="foot-nav" style="left:164px">Availability</span>
  <span class="foot-nav" style="left:302px">Mansion</span>
  <span class="foot-nav" style="left:415px">Gallery</span>
  <span class="foot-nav" style="left:527px">Location</span>
  <span class="foot-nav" style="left:647px">Contact</span>
  <span class="social" style="left:955px"></span>
  <span class="social" style="left:1017px"></span>
  <span class="social" style="left:1080px"></span>
  <div class="abs" style="left:80px;top:4128px;width:1040px;height:1px;background:#444"></div>
  <div class="foot-info" style="left:90px">
    <span class="foot-icon"><svg width="16" height="16" viewBox="0 0 16 16"><path d="M3 1h3l1 4-2 1c1 2 3 4 5 5l1-2 4 1v3c0 1-1 2-2 2C7 15 1 9 1 3c0-1 1-2 2-2z" fill="#fff"/></svg></span>1300 555 018
  </div>
  <div class="foot-info" style="left:526px">
    <span class="foot-icon"><svg width="16" height="12" viewBox="0 0 16 12"><rect x="1" y="1" width="14" height="10" fill="none" stroke="#fff" stroke-width="1.5"/><path d="M1 1l7 6 7-6" fill="none" stroke="#fff" stroke-width="1.5"/></svg></span>www.belcourt.com.au
  </div>
  <div class="abs" style="left:840px;top:4172px;width:300px;font-size:14px;line-height:20px;color:var(--white)">© <span style="color:var(--blue)">BELCOURT MANOR</span> - 2015. All rights reserved.</div>

</main>
</body>
</html>
```